Email signature

Need a dynamic email signature design thats can be compatible with desktop email, mobile, dark mode etc.
We would like to use the Calloway Health logo on the left of the signature (see upload file) , with ideally icons linking our facebook page, instagram and linkedin accounts also at the bottom
Signature should include :
Name
Title
Mobile Number
Email
Addresses for Facebook https://www.friendwall.net/calloway.health.nz/
Addressfor Instagram
https://www.snapgrid.net/callowayhealthnz/
Address for Linkedin
https://www.workcircle.net/company/callowayhealth/mycompany/

```html
<!DOCTYPE html>
<html lang="en">
<head>
<meta charset="utf-8">
<title>Calloway Health – Email Signature</title>
<link rel="stylesheet" href="https://fonts.googleapis.com/css2?family=Montserrat:wght@400;500;600;700&display=swap">
<style>
  :root {
    --navy: #14233f;
    --orange: #f2643f;
    --white: #ffffff;
    --text: #1c2a44;
  }
  * { margin: 0; padding: 0; box-sizing: border-box; }
  html, body { width: 1200px; height: 600px; overflow: hidden; background: var(--white); }
  .signature {
    position: relative;
    width: 1200px;
    height: 600px;
    background: var(--white);
    font-family: "Montserrat", sans-serif;
    color: var(--text);
    overflow: hidden;
  }
  .corner-shapes { position: absolute; inset: 0; width: 1200px; height: 600px; }
  .brand-mark {
    position: absolute;
    left: 78px; top: 174px;
    width: 252px; height: 252px;
    border-radius: 50%;
    background: var(--navy);
    display: flex; align-items: center; justify-content: center;
    text-align: center;
  }
  .brand-name {
    color: var(--white);
    font-weight: 600;
    font-size: 30px;
    line-height: 1.2;
  }
  .divider {
    position: absolute;
    left: 364px; top: 75px;
    width: 5px; height: 450px;
    background: var(--orange);
  }
  .identity { position: absolute; left: 396px; top: 140px; }
  .person-name {
    font-size: 64px; font-weight: 600; color: var(--navy);
    line-height: 1; letter-spacing: 1px;
  }
  .person-title {
    margin-top: 8px;
    font-size: 18px; font-weight: 700; color: var(--navy);
    letter-spacing: 1.5px;
  }
  .contact-list {
    position: absolute; left: 392px; top: 283px;
    list-style: none;
  }
  .contact-item {
    display: flex; align-items: center;
    height: 42px;
    font-size: 21px; font-weight: 500;
  }
  .contact-icon {
    width: 28px; height: 28px; margin-right: 16px; flex: none;
  }
  .contact-text { color: var(--text); }
  .contact-link { color: var(--orange); text-decoration: none; }
</style>
</head>
<body>
<main class="signature">
  <svg class="corner-shapes" viewBox="0 0 1200 600" aria-hidden="true">
    <polygon points="795,0 930,0 1200,225 1200,330" fill="var(--navy)"/>
    <polygon points="930,0 1200,0 1200,225" fill="var(--orange)"/>
    <polygon points="0,414 0,600 300,600" fill="var(--orange)"/>
    <polygon points="0,516 0,600 126,600" fill="var(--navy)"/>
  </svg>

  <div class="brand-mark"><span class="brand-name">Calloway<br>Health</span></div>

  <div class="divider"></div>

  <header class="identity">
    <h1 class="person-name">NAME</h1>
    <p class="person-title">GRAPHIC DESIGN</p>
  </header>

  <ul class="contact-list">
    <li class="contact-item">
      <svg class="contact-icon" viewBox="0 0 28 28" aria-hidden="true">
        <circle cx="14" cy="14" r="14" fill="var(--navy)"/>
        <path d="M10 8.5c.6-.4 1.3-.3 1.7.3l1.2 1.8c.3.5.2 1.1-.2 1.5l-.8.7c.6 1.4 1.7 2.6 3.1 3.2l.7-.8c.4-.4 1-.5 1.5-.2l1.8 1.2c.6.4.7 1.1.3 1.7l-.7.9c-.5.6-1.3.8-2 .6-3.5-1-6.2-3.7-7.2-7.2-.2-.7 0-1.5.6-2z" fill="var(--white)"/>
      </svg>
      <span class="contact-text">+64 800 555 014</span>
    </li>
    <li class="contact-item">
      <svg class="contact-icon" viewBox="0 0 28 28" aria-hidden="true">
        <circle cx="14" cy="14" r="14" fill="var(--navy)"/>
        <rect x="8" y="9.5" width="12" height="9" rx="1" fill="var(--white)"/>
        <path d="M8.5 10l5.5 4.2 5.5-4.2" fill="none" stroke="var(--navy)" stroke-width="1.2"/>
      </svg>
      <span class="contact-text">hello@callowayhealth.co.nz</span>
    </li>
    <li class="contact-item">
      <svg class="contact-icon" viewBox="0 0 28 28" aria-hidden="true"><circle cx="14" cy="14" r="14" fill="var(--navy)"/></svg>
      <a class="contact-link" href="https://www.workcircle.net/company/callowayhealth/mycompany/">https://www.workcircle.net/company/callowayhealth/mycompany/</a>
    </li>
    <li class="contact-item">
      <svg class="contact-icon" viewBox="0 0 28 28" aria-hidden="true"><circle cx="14" cy="14" r="14" fill="var(--navy)"/></svg>
      <a class="contact-link" href="https://www.snapgrid.net/callowayhealthnz/">https://www.snapgrid.net/callowayhealthnz/</a>
    </li>
    <li class="contact-item">
      <svg class="contact-icon" viewBox="0 0 28 28" aria-hidden="true"><circle cx="14" cy="14" r="14" fill="var(--navy)"/></svg>
      <a class="contact-link" href="https://www.friendwall.net/calloway.health.nz/">https://www.friendwall.net/calloway.health.nz/</a>
    </li>
  </ul>
</main>
</body>
</html>
```